Construction company looking for modern

**Tallow Crest Joinery Limited**

We need a website for a renovation/remodeling company based in Hamilton, New Zealand. Ideally it will catch clients' attention and be modern and professional looking. I have attached a logo that I have just recently had made (through PixelHarbor). If the website could reflect this style and colour schemes, that would be awesome. The final design should communicate a trustworthiness and professionalism.

I have attached photos of a website that I really think is great, so if we could have something that follows along those likes,

https://www.dailyplover.example/local-news/news/local-builder-named-top-apprentice-for-region/QZTRPLA8VXN2MJ5DFYUEKHSWGO/

I won a competition a few years ago while I was an apprentice, If we could somehow put that in there as one of my achievements to try to bring in some trust that would be awesome. I would like to add a new picture though because my beard in that photo is wild.

Target Market(s)

Families that want live in the homes that i'm working on. not investors. People that are looking for quality not cheapest price.

Industry/Entity Type

Construction, Home renovations, Maintenance, Deck Builds, New Builds, Bathrooms, Kitchens

Coding

Coded - Design and coding required

Number of Pages Required

5+ page

Font styles to use
Sans Serif

Colors
6B429C
8869AF
B7A5CE
E3DAEB
F3F0F8

Requirements
Must have
• Contact us page, large clear pictures, Colours the work with the purple in my logo. That will be my company colour so I'm thinking black and purple, or what ever compliments purple nicely
Nice to have
• Page for Renovations, Testimonials, Contact us, Home, About us
Should not have
• Plain looking pages, empty white space, I want the text to be beside a nice big picture etc

```html
<!DOCTYPE html>
<html lang="en">
<head>
<meta charset="utf-8">
<title>Tallow Crest Joinery Limited</title>
<link href="https://fonts.googleapis.com/css2?family=Marcellus&family=Montserrat:wght@400;500;600&display=swap" rel="stylesheet">
<style>
:root{
  --purple:#6b429c;
  --purple-mid:#8869af;
  --purple-soft:#b7a5ce;
  --lavender:#e3daeb;
  --mist:#f3f0f8;
  --ink:#1d1d1f;
  --text:#4a4a4a;
  --white:#fff;
}
*{box-sizing:border-box;margin:0;padding:0}
html,body{width:1200px;height:5059px;overflow:hidden}
body{position:relative;background:var(--white);font-family:'Montserrat',sans-serif;color:var(--ink)}
.abs{position:absolute}
a{color:inherit;text-decoration:none}

/* top bar */
.topbar{left:0;top:0;width:1200px;height:43px;background:var(--purple);color:#fff;font-size:11px;display:flex;justify-content:flex-end;align-items:center;gap:20px;padding-right:118px}
.brand{left:122px;top:62px;display:flex;align-items:center;gap:8px;color:var(--purple);font-size:12px;font-weight:600;line-height:1.2;width:100px}
.brand-mark{width:14px;height:14px;background:var(--purple);flex:none}
.menu{left:253px;top:81px;display:flex;gap:21px;font-size:14px;font-weight:500}
.nav-icons{left:1016px;top:78px;display:flex;gap:14px;align-items:center}

/* photo areas */
.photo{overflow:hidden}
.hero-photo{left:204px;top:143px;width:878px;height:625px;
  background:linear-gradient(100deg,#f3f2f0 0%,#e6e4e0 22%,#c9b08a 30%,#ecebe8 38%,#f4f4f2 50%,#5d6468 60%,#3a3f44 72%,#c8c6c2 86%,#6e5c4c 100%)}
.hero-frame{left:177px;top:668px;width:121px;height:125px;border:1.5px solid var(--purple-mid)}
.hero-box{left:0;top:212px;width:475px;height:424px;background:var(--purple);color:#fff;padding:50px 40px 0 42px}
.hero-box h1{font-family:'Marcellus',serif;font-weight:400;font-size:55px;line-height:68px}
.hero-box p{margin-top:22px;font-size:17.5px;line-height:31px;color:#eee6f6;width:400px}
.hero-scroll{left:864px;top:717px;width:98px;height:94px;background:var(--purple)}
.slider-ctrl{left:1124px;top:290px;width:32px;text-align:center;color:#333;font-size:15px}

/* services */
.services{left:0;top:870px;width:1200px;height:426px;background:linear-gradient(90deg,#f2f2f1,#fafafa 40%,#efefee)}
.service{width:290px;text-align:center}
.service h3{font-family:'Marcellus',serif;font-weight:400;color:var(--purple);font-size:33px;margin-top:22px}
.service p{font-family:'Marcellus',serif;font-size:19px;line-height:32px;color:#222;margin:14px auto 0;width:280px}

/* experience */
.exp-photo{left:120px;top:1434px;width:450px;height:609px;
  background:linear-gradient(180deg,#9a9ca0 0%,#6d7075 25%,#3e4146 50%,#5a4a36 68%,#2a2824 82%,#16171a 100%)}
.exp-sketch{left:560px;top:1780px;width:640px;height:340px;background:linear-gradient(90deg,rgba(243,240,248,0),rgba(243,240,248,.5))}
.exp h2{font-weight:500;font-size:45px;line-height:68px;color:var(--ink)}
.exp p{font-size:20px;line-height:35px;color:#555;margin-top:22px;width:510px}
.stats{display:flex;margin-top:30px}
.stat{width:162px}
.stat b{display:block;font-weight:400;font-size:54px;line-height:58px}
.stat span{display:block;font-size:19px;line-height:24px;color:#333}
.btn{display:flex;align-items:center;border:2px solid var(--purple);color:var(--purple);font-size:19px;font-weight:500;height:65px;padding-left:22px;position:relative}
.btn svg{position:absolute;right:-18px;top:25px}

/* features */
.feature{left:118px;width:440px}
.feature h3{font-weight:400;font-size:28px;display:flex;gap:22px}
.feature h3 em{font-style:normal;font-weight:600}
.feature p{font-size:13.5px;line-height:23px;color:#555;margin:16px 0 0 62px}

/* portfolio */
.portfolio{left:0;top:2917px;width:1200px;height:811px;background:var(--mist)}
.ghost{left:116px;top:2955px;font-size:78px;font-weight:600;color:#ede8f4}
.card{top:3139px;width:279px;height:477px}
.cap{position:absolute;background:#fff;padding:14px 22px}
.cap h4{color:var(--purple);font-weight:600;font-size:16px}
.cap p{font-size:11px;color:#666;margin-top:6px;line-height:16px}
.cap small{display:flex;align-items:center;gap:6px;font-size:10.5px;color:#666;margin-top:8px}

/* testimonial */
.house{left:0;top:3728px;width:652px;height:505px;
  background:linear-gradient(180deg,#6f9fd8 0%,#b9d0ec 28%,#e8eef4 36%,#6a5a4c 44%,#b79a78 56%,#8a7a66 64%,#6f9a3c 72%,#4f7e2a 100%)}
.quote{left:691px;top:3828px}
.quote h2{font-weight:600;color:var(--purple);font-size:35px;margin-top:14px}
.quote p{font-size:14px;line-height:30px;color:#555;margin-top:18px;width:390px}
.quote .name{font-size:14px;font-weight:600;margin-top:20px;color:#222}
.quote .role{font-size:13px;color:#777;margin-top:6px}
.arrows{display:flex;gap:8px;margin-top:16px}
.arrows span{width:30px;height:26px;border:1.5px solid var(--purple);display:flex;align-items:center;justify-content:center;color:var(--purple);font-size:14px}

/* cta */
.cta{left:0;top:4233px;width:1200px;height:490px}
.cta-inner{left:0;top:4320px;width:1200px;text-align:center;color:#fff}
.cta-inner h2{font-weight:500;font-size:34px}
.cta-inner p{font-size:14px;line-height:29px;margin:34px auto 0;width:690px;color:#efe8f7}
.btn-light{left:495px;top:4523px;width:187px;height:55px;border:2px solid #fff;color:#fff;font-size:18px;display:flex;align-items:center;padding-left:24px}

/* footer */
.f-brand{left:122px;top:4745px;display:flex;align-items:center;gap:10px;color:var(--purple);font-weight:600;font-size:17px;line-height:1.25;width:200px}
.f-brand i{width:18px;height:18px;background:var(--purple);flex:none}
.f-info{left:122px;font-size:12.5px;line-height:24px;color:#333;display:flex;gap:10px}
.f-links{display:flex;gap:18px;font-size:12.5px;color:#222;right:118px}
.rule{height:1px;background:#cfcfcf}
.copy{left:0;top:5024px;width:1200px;text-align:center;font-size:12.5px;color:#333}
</style>
</head>
<body>

<div class="abs topbar">
  <span>How it works</span><span>Virtual Tour</span><span>Portfolio</span><span>Contact us</span><span>|</span><span>(07) 555 0142</span>
</div>

<div class="abs brand"><span class="brand-mark"></span><span>Tallow Crest Joinery</span></div>
<nav class="abs menu">
  <a>Construction</a><a>Home Renovations</a><a>Maintenance</a><a>Deck Builds</a><a>New Builds</a><a>Bathrooms</a>
</nav>
<div class="abs nav-icons">
  <svg width="22" height="22" viewBox="0 0 22 22"><circle cx="9" cy="9" r="6.5" fill="none" stroke="#111" stroke-width="3"/><line x1="14" y1="14" x2="20" y2="20" stroke="#111" stroke-width="3.2" stroke-linecap="round"/></svg>
  <svg width="26" height="22" viewBox="0 0 26 22"><rect y="1" width="26" height="3.4" fill="#111"/><rect y="9.3" width="26" height="3.4" fill="#111"/><rect y="17.6" width="26" height="3.4" fill="#111"/></svg>
</div>

<!-- hero -->
<div class="abs hero-frame"></div>
<div class="abs photo hero-photo" role="img" aria-label="Large photo: modern bathroom with white marble walls, glass shower screen, timber vanity and dark tiled floor"></div>
<section class="abs hero-box">
  <h1>We Help You Make Modern Interior</h1>
  <p>We will help you to make an elegant and luxurious interior designed by professional interior designers.</p>
</section>
<div class="abs hero-scroll">
  <svg width="98" height="94" viewBox="0 0 98 94"><line x1="49" y1="30" x2="49" y2="62" stroke="#fff" stroke-width="1.5"/><circle cx="49" cy="64" r="3" fill="#fff"/></svg>
</div>
<div class="abs slider-ctrl">
  <svg width="24" height="14" viewBox="0 0 24 14"><polyline points="3,12 12,3 21,12" fill="none" stroke="#333" stroke-width="3"/></svg>
  <svg width="24" height="14" viewBox="0 0 24 14" style="margin-top:62px"><polyline points="3,2 12,11 21,2" fill="none" stroke="#333" stroke-width="3"/></svg>
  <div style="margin-top:104px">01</div>
  <div style="width:1px;height:50px;background:#999;margin:6px auto"></div>
  <div>06</div>
</div>

<!-- services -->
<section class="abs services"></section>
<div class="abs service" style="left:123px;top:970px">
  <svg width="56" height="56" viewBox="0 0 56 56" fill="none" stroke="#222" stroke-width="2.2"><path d="M6 28 L28 8 L50 28"/><path d="M12 24 V50 H44 V24"/><rect x="22" y="34" width="12" height="16"/><path d="M40 14 V8 H45 V18"/></svg>
  <h3>New Builds</h3>
  <p>Lorem Ipsum is simply dummy text of the printing and typesetting industry.</p>
</div>
<div class="abs service" style="left:455px;top:970px">
  <svg width="56" height="56" viewBox="0 0 56 56" fill="none" stroke="#222" stroke-width="2.2"><path d="M10 46 L36 20"/><circle cx="41" cy="15" r="8"/><path d="M46 46 L20 20"/><path d="M10 10 L16 8 L22 14 L20 20 L14 22 L8 16 Z"/><path d="M42 42 L48 48"/></svg>
  <h3>Renovations</h3>
  <p>Lorem Ipsum is simply dummy text of the printing and typesetting industry.</p>
</div>
<div class="abs service" style="left:787px;top:970px">
  <svg width="56" height="56" viewBox="0 0 56 56" fill="none" stroke="#222" stroke-width="2.2"><circle cx="28" cy="28" r="22"/><path d="M14 30 L28 17 L42 30"/><path d="M19 27 V40 H37 V27"/><rect x="25" y="32" width="6" height="8"/></svg>
  <h3>Roofing</h3>
  <p>Lorem Ipsum is simply dummy text of the printing and typesetting industry.</p>
</div>

<!-- experience -->
<div class="abs exp-sketch" role="img" aria-label="Faint architectural line sketch of a house"></div>
<div class="abs photo exp-photo" role="img" aria-label="Large photo: high-rise building under construction with a tower crane against a stormy dusk sky and lit city streets"></div>
<section class="abs exp" style="left:599px;top:1459px">
  <h2>We Provide You The<br>Best Experience</h2>
  <p>Lorem Ipsum is simply dummy text of the printing and typesetting industry. Lorem Ipsum has been the industry's standard dummy text ever since the 1500s</p>
  <div class="stats">
    <div class="stat"><b>10</b><span>Years<br>Experience</span></div>
    <div class="stat"><b>01</b><span>Award<br>Gained</span></div>
    <div class="stat"><b>500</b><span>Material<br>Sold</span></div>
  </div>
  <a class="btn" style="width:177px;margin-top:42px">Learn More
    <svg width="52" height="12" viewBox="0 0 52 12"><line x1="0" y1="6" x2="48" y2="6" stroke="#6b429c" stroke-width="2"/><polyline points="42,1 49,6 42,11" fill="none" stroke="#6b429c" stroke-width="2"/></svg></a>
</section>

<!-- features -->
<div class="abs feature" style="top:2288px"><h3><em>01</em>All-in-One Experience</h3><p>Lorem Ipsum is simply dummy text of the printing and typesetting industry. Lorem Ipsum has been the industry's standard dummy text ever since the 1500s.</p></div>
<div class="abs feature" style="top:2435px"><h3><em>02</em>Stunning Design</h3><p>Lorem Ipsum is simply dummy text of the printing and typesetting industry. Lorem Ipsum has been the industry's standard dummy text ever since the 1500s.</p></div>
<div class="abs feature" style="top:2580px"><h3><em>03</em>Quality Material</h3><p>Lorem Ipsum is simply dummy text of the printing and typesetting industry. Lorem Ipsum has been the industry's standard dummy text ever since the 1500s.</p></div>
<a class="abs btn" style="left:120px;top:2744px;width:153px;height:64px">See More
  <svg width="52" height="12" viewBox="0 0 52 12"><line x1="0" y1="6" x2="48" y2="6" stroke="#6b429c" stroke-width="2"/><polyline points="42,1 49,6 42,11" fill="none" stroke="#6b429c" stroke-width="2"/></svg></a>
<div class="abs photo" style="left:568px;top:2268px;width:265px;height:157px;background:linear-gradient(180deg,#f2f2f0 0%,#dcdcda 45%,#8e8c88 62%,#e2b23a 78%,#6a5a48 100%)" role="img" aria-label="Photo: white kitchen with fresh produce on the benchtop"></div>
<div class="abs photo" style="left:841px;top:2268px;width:241px;height:360px;background:linear-gradient(180deg,#f7f7f5 0%,#ecebe7 40%,#b9b19f 62%,#dcd7cc 80%,#efece6 100%)" role="img" aria-label="Photo: bright corner with arc floor lamp, wooden chair and potted plant"></div>
<div class="abs photo" style="left:564px;top:2439px;width:269px;height:369px;background:linear-gradient(180deg,#f1f0ee 0%,#a7998a 35%,#8b7c6c 52%,#f3f3f1 66%,#e8e7e4 78%,#7a4e34 100%)" role="img" aria-label="Photo: kitchen island with glass pendant lights, taupe cabinets and timber stools"></div>
<div class="abs photo" style="left:841px;top:2642px;width:241px;height:166px;background:linear-gradient(180deg,#f4f4f2 0%,#e4e2dc 55%,#bfae94 80%,#ecebe8 100%)" role="img" aria-label="Photo: light dining nook with wooden chairs"></div>

<!-- portfolio -->
<section class="abs portfolio"></section>
<div class="abs ghost">Portfolio</div>
<div class="abs" style="left:120px;top:2998px">
  <h2 style="font-weight:500;font-size:31px">Our Portfolio</h2>
  <p style="font-size:13.5px;line-height:23px;color:#555;margin-top:10px;width:420px">Lorem Ipsum is simply dummy text of the printing and typesetting industry.</p>
</div>
<div class="abs card photo" style="left:0;background:linear-gradient(180deg,#f0f1f2 0%,#c9c6c2 18%,#a4583a 36%,#d98a3a 48%,#6d6a66 62%,#8c4a2e 80%,#5c5048 100%)" role="img" aria-label="Photo: builder in safety gear and hi-vis vest working on steel framing">
  <div class="cap" style="left:25px;top:377px;width:229px;height:66px"><h4>Construction Work</h4><small>Read More <svg width="22" height="6" viewBox="0 0 22 6"><line x1="0" y1="3" x2="20" y2="3" stroke="#666"/><polyline points="17,0.5 21,3 17,5.5" fill="none" stroke="#666"/></svg></small></div>
</div>
<div class="abs card photo" style="left:306px;background:linear-gradient(120deg,#f6f5f3 0%,#ebe7e1 45%,#d6b9a0 62%,#efece8 80%,#d8d2ca 100%)" role="img" aria-label="Photo: hand fitting a plate to a freshly plastered wall">
  <div class="cap" style="left:29px;top:339px;width:232px;height:119px"><h4>Home Renovations</h4><p>Lorem Ipsum is simply dummy text of the printing and typesetting industry.</p></div>
</div>
<div class="abs card photo" style="left:613px;background:linear-gradient(180deg,#f6f6f6 0%,#e6e7e8 30%,#cfd3d4 55%,#4f9a96 66%,#c8c9c8 78%,#9a9c9c 100%)" role="img" aria-label="Photo: white kitchen with glass-front cabinets, range hood and teal cooking pot">
  <div class="cap" style="left:25px;top:382px;width:237px;height:75px"><h4>Kitchens</h4><small>Read More <svg width="22" height="6" viewBox="0 0 22 6"><line x1="0" y1="3" x2="20" y2="3" stroke="#666"/><polyline points="17,0.5 21,3 17,5.5" fill="none" stroke="#666"/></svg></small></div>
</div>
<div class="abs card photo" style="left:921px;background:linear-gradient(180deg,#f8f8f8 0%,#eeeeec 40%,#dedcd6 60%,#7f9656 74%,#ebebea 88%,#d0cfcc 100%)" role="img" aria-label="Photo: white bathroom with pedestal basin, mirror and trailing plant">
  <div class="cap" style="left:25px;top:382px;width:254px;height:75px"><h4>Bathrooms</h4><small>Read More <svg width="22" height="6" viewBox="0 0 22 6"><line x1="0" y1="3" x2="20" y2="3" stroke="#666"/><polyline points="17,0.5 21,3 17,5.5" fill="none" stroke="#666"/></svg></small></div>
</div>

<!-- testimonial -->
<div class="abs photo house" role="img" aria-label="Large photo: new family home with stone and timber facade, double garage and green lawn under blue sky"></div>
<section class="abs quote">
  <svg width="78" height="66" viewBox="0 0 78 66" fill="none" stroke="#999" stroke-width="2.5"><path d="M4 62 V30 Q4 6 30 4 V16 Q16 18 16 30 H30 V62 Z"/><path d="M44 62 V30 Q44 6 70 4 V16 Q56 18 56 30 H70 V62 Z"/></svg>
  <h2>What our Client Say</h2>
  <p>Lorem Ipsum is simply dummy text of the printing and typesetting industry. Lorem Ipsum has been the industry's standard dummy text ever since the 1500s.</p>
  <div class="name">Aroha Kettering</div>
  <div class="role">Customer</div>
  <div class="arrows"><span>&larr;</span><span>&rarr;</span></div>
</section>

<!-- cta -->
<svg class="abs cta" width="1200" height="490" viewBox="0 0 1200 490" preserveAspectRatio="none">
  <path d="M0 0 H1200 V430 Q1080 420 960 455 Q760 505 560 450 Q380 410 200 460 Q100 485 0 470 Z" fill="#6b429c"/>
</svg>
<section class="abs cta-inner">
  <h2>Ready for Renovation / Remodeling?</h2>
  <svg width="150" height="10" viewBox="0 0 150 10" style="margin-top:18px"><line x1="4" y1="5" x2="146" y2="5" stroke="#fff" stroke-width="2"/><circle cx="4" cy="5" r="3.5" fill="#fff"/><circle cx="146" cy="5" r="3.5" fill="#fff"/></svg>
  <p>Lorem Ipsum is simply dummy text of the printing and typesetting industry. Lorem Ipsum has been the industry's standard dummy text ever since the 1500s.</p>
</section>
<a class="abs btn-light">Free Quote
  <svg width="52" height="12" viewBox="0 0 52 12" style="position:absolute;right:-20px;top:20px"><line x1="0" y1="6" x2="48" y2="6" stroke="#fff" stroke-width="2"/><polyline points="42,1 49,6 42,11" fill="none" stroke="#fff" stroke-width="2"/></svg></a>

<!-- footer -->
<div class="abs f-brand"><i></i><span>Tallow Crest Joinery</span></div>
<div class="abs f-info" style="top:4850px">
  <svg width="20" height="26" viewBox="0 0 20 26"><path d="M10 1 C4.5 1 1 5 1 10 C1 17 10 25 10 25 C10 25 19 17 19 10 C19 5 15.5 1 10 1 Z" fill="#6b429c"/><circle cx="10" cy="10" r="3.5" fill="#fff"/></svg>
  <div>14 Marram Lane, Ferndale<br>Hamilton 3214</div>
</div>
<div class="abs f-info" style="top:4921px">
  <svg width="20" height="22" viewBox="0 0 20 22"><path d="M4 2 L8 2 L9.5 7 L7 9 Q9 14 13 15.5 L15 13 L19 15 L19 19 Q17 21 14 20.5 Q4 17 1.5 6 Q1.5 3 4 2 Z" fill="#6b429c"/></svg>
  <div>Sales: (07) 555 0142<br>Delivery: (07) 555 0143</div>
</div>
<nav class="abs f-links" style="top:4834px"><a>How it works</a><a>Virtual Tour</a><a>Portfolio</a><a>Contact us</a><span>|</span><a>(07) 555 0142</a></nav>
<div class="abs rule" style="left:467px;top:4871px;width:615px"></div>
<nav class="abs f-links" style="top:4900px"><a>Construction</a><a>Home Renovations</a><a>Maintenance</a><a>Deck Builds</a><a>New Builds</a><a>Bathrooms</a></nav>
<div class="abs rule" style="left:118px;top:5004px;width:964px"></div>
<div class="abs copy">Copyright 2023 | Tallow Crest Joinery Limited</div>

</body>
</html>
```